Brookfern Clinical Trials Redesign

Website name: http://brookfernclinicaltrials.example/live/
Industry: medical & pharmaceutical
Target audience:
Clinical research patients
clinical research sponsors
clinical research referring doctors
Style/theme of your website design:
We want to customize the orbitel theme, emulating our competitors website
http://templatemarket.example/item/orbitel-responsive-multipurpose-wordpress-theme/4417203
Webdesign Examples?
http://www.tmxclinical.example/currently-enrolling-clinical-trials/
https://www.copperwellresearch.example/
What do you like about these sites:
These sites address all the needs of a clinical trial facility. The patient, the doctor and the sponsor. Also they have forms and sign up information for each trial they offer. The site needs to have SCHEMA markup and rich snippets. We have reviews and testimonial that need schema markup also, local NAP information and all the other rich snippet markups available.
How many pages need design:
8-12
List any colors:
existing color of website and logo
Target Market(s)
Target audience:
Industry/Entity Type
Pharmaceutical
Number of Pages Required
5+ page
Look and feel

```html
<!DOCTYPE html>
<html lang="en">
<head>
<meta charset="utf-8">
<title>Brookfern Clinical Trials</title>
<link rel="stylesheet" href="https://fonts.googleapis.com/css2?family=Open+Sans:wght@400;600;700&display=swap">
<style>
:root{
  --lime:#d6e021;
  --green:#3cb54a;
  --nav-top:#8dc63f;
  --nav-bottom:#6cb23a;
  --nav-active:#0d7a5b;
  --teal:#1a9e98;
  --red:#c4122f;
  --text:#555555;
  --dark:#222222;
  --news-green:#1e9a3c;
  --border:#dcdcdc;
  --footer:#58585a;
  --footer-text:#ffffff;
  --footer-head:#d6e021;
}
*{box-sizing:border-box;margin:0;padding:0}
html,body{width:1087px;height:1200px;overflow:hidden;background:#fff}
body{font-family:"Open Sans",Arial,sans-serif;color:var(--text);position:relative}
a{text-decoration:none}
.page{position:relative;width:1087px;height:1200px;overflow:hidden}
.backdrop{position:absolute;left:0;top:0;width:1087px;height:580px}
.abs{position:absolute}

.site-header{left:118px;top:16px;width:851px;height:95px;background:linear-gradient(180deg,#ffffff 0%,#f1f1f1 100%)}
.brand{left:10px;top:22px;display:flex;align-items:center;gap:8px}
.brand-mark{width:44px;height:44px;border-radius:50%;background:var(--teal)}
.brand-name{font-weight:600;font-size:19px;line-height:19px;color:var(--teal)}
.call{right:10px;top:24px;text-align:left}
.call-label{display:flex;align-items:center;gap:8px;font-size:14px;font-weight:600;color:var(--news-green)}
.call-number{font-size:24px;font-weight:600;color:var(--red);margin-left:24px;line-height:30px}

.main-nav{left:118px;top:119px;width:851px;height:43px;background:linear-gradient(180deg,var(--nav-top),var(--nav-bottom));display:flex}
.main-nav a{color:#fff;font-size:13.5px;font-weight:600;line-height:43px;padding:0 16px}
.main-nav a.active{background:var(--nav-active);padding:0 21px}

.hero{left:118px;top:170px;width:851px;height:331px;border:2px solid #fff;background:linear-gradient(90deg,#9fd3ee 0%,#2f8fd0 40%,#0c5aa8 75%,#06306a 100%)}
.slider-dots{left:498px;top:526px;display:flex;gap:7px}
.slider-dots span{width:18px;height:18px;border-radius:50%;background:#fff}
.slider-dots span.on{background:var(--lime)}

h2{font-weight:400;color:var(--red);font-size:19px}
p{font-size:12px;line-height:21px}
.more{font-size:12.5px;font-weight:600;color:var(--dark)}

.welcome{left:119px;top:602px;width:480px}
.welcome p{margin-top:9px}
.btn{left:118px;top:743px;width:100px;height:33px;background:var(--green);color:#fff;font-size:12.5px;font-weight:600;line-height:33px;text-align:center;border-radius:2px}

.news{left:625px;top:602px;width:344px;height:174px;border:1px solid var(--border);background:linear-gradient(180deg,#f4f4f4,#fff 60%);padding:12px 18px 12px 21px}
.news-dots{right:14px;top:20px;display:flex;gap:5px}
.news-dots span{width:11px;height:11px;background:#b8b8b8;border-radius:2px}
.news-dots span.on{background:#7cbf3c}
.news-date{font-size:12.5px;font-weight:600;color:var(--news-green);margin-top:10px}
.news p{margin-top:2px}
.news .more{display:block;margin-top:8px}

.research-band{left:118px;top:804px;width:851px;height:228px;background:linear-gradient(180deg,#f3f3f3,#fafafa);border-top:1px solid var(--border)}
.research-title{left:139px;top:822px}
.research-img{left:139px;top:863px;width:175px;height:131px;background:linear-gradient(135deg,#e8f4fc,#9fcdee 55%,#5aa6dc)}
.research-text{left:336px;top:858px;width:338px}
.research-text .more{display:block;margin-top:11px}

.blog{left:697px;top:824px;width:259px;height:168px;background:#fff;border:1px solid var(--border);border-radius:3px;padding:12px 16px;box-shadow:0 6px 8px -6px rgba(0,0,0,.25)}
.blog-thumb{left:17px;top:51px;width:48px;height:48px;background:var(--teal)}
.blog-post{left:81px;top:46px;width:168px}
.blog-post h3{font-size:12.5px;font-weight:600;color:var(--news-green);line-height:20px}
.blog-post .more{display:block;margin-top:9px}

.site-footer{left:0;top:1032px;width:1087px;height:168px;background:var(--footer)}
.fcol{top:22px}
.fcol h4{font-size:14px;font-weight:600;color:var(--footer-head);margin-bottom:8px}
.fcol ul{list-style:none}
.fcol li{font-size:11.5px;color:var(--footer-text);line-height:26.3px;display:flex;align-items:center;gap:10px}
.sicon{width:14px;height:14px;border-radius:2px;background:#3d7bbf}
.sicon.rss{background:#f07f1a}
.sicon.chirp{background:#4fb3e6}
.flogo{left:778px;top:52px;display:flex;align-items:center;gap:7px}
.flogo .brand-mark{width:36px;height:36px}
.flogo .brand-name{font-size:15px;line-height:15px}
.copyright{left:696px;top:119px;font-family:Arial,Helvetica,sans-serif;font-size:13px;color:#fff}
</style>
</head>
<body>
<div class="page">
  <svg class="backdrop" width="1087" height="580" viewBox="0 0 1087 580" aria-hidden="true">
    <rect width="1087" height="344" fill="#d6e021"/>
    <path d="M0 344 H1087 V486 Q543 650 0 486 Z" fill="#3cb54a"/>
  </svg>

  <header class="site-header abs">
    <div class="brand abs">
      <span class="brand-mark"></span>
      <span class="brand-name">Brookfern<br>Clinical<br>Trials</span>
    </div>
    <div class="call abs">
      <div class="call-label">
        <svg width="15" height="15" viewBox="0 0 15 15" aria-hidden="true"><rect width="15" height="15" rx="3" fill="#555"/><path d="M4.5 3.5c-.8.4-1 1.4-.6 2.6.8 2.3 2.6 4.2 4.8 5.2 1.1.5 2.1.3 2.6-.5l-1.6-1.6-1.2.7c-1-.5-2-1.5-2.5-2.6l.7-1.1z" fill="#fff"/></svg>
        Call Us:
      </div>
      <div class="call-number">121 555 0147</div>
    </div>
  </header>

  <nav class="main-nav abs">
    <a class="active" href="#">HOME</a>
    <a href="#">LOCATIONS</a>
    <a href="#">RESEARCH</a>
    <a href="#">SORT ME OUT</a>
    <a href="#">SOCIAL</a>
    <a href="#">BLOG</a>
    <a href="#">BIO</a>
    <a href="#">CONTACT US</a>
  </nav>

  <div class="hero abs" role="img" aria-label="Researcher writing notes on a clipboard beside racks of coloured test tubes in a blue-lit laboratory"></div>
  <div class="slider-dots abs"><span class="on"></span><span></span><span></span><span></span></div>

  <section class="welcome abs">
    <h2>Welcome to Our Website</h2>
    <p>Aliquam nibh ante, egestas id dictum a, commodo luctus libero. Praesent faucibus malesuada faucibus. Donecyl laoreet metus id laoreet malesuada. Lorem ipsum dolor sit amet, consectetur adipiscing elit. Nullam consectetu orci sed nulla facilisis consequat. Curabitur vel lorem sit amet nulla ullamcorper fermentum.</p>
  </section>
  <a class="btn abs" href="#">READ MORE</a>

  <aside class="news abs">
    <h2>Latest News</h2>
    <div class="news-dots abs"><span class="on"></span><span></span><span></span></div>
    <div class="news-date">DEC 10, 2013</div>
    <p>Aliquam nibh ante, egestas id dictum a, commodo luctus libero. Praesent faucibus malesuada faucibus. Donecy laoreet metus id laoreet malesuada...</p>
    <a class="more" href="#">READ MORE</a>
  </aside>

  <div class="research-band abs"></div>
  <h2 class="research-title abs">Our Research</h2>
  <div class="research-img abs" role="img" aria-label="Hand touching a glowing digital display of medical icons"></div>
  <div class="research-text abs">
    <p>Aliquam nibh ante, egestas id dictum a, commodo luctus libero. Praesent faucibus malesuada faucibus. Donecyl laoreet metus id laoreet malesuada. Lorem ipsum dolor sit amet, consectetur adipiscing elit. Nullam consectetu orci sed nulla facilisis consequat.</p>
    <a class="more" href="#">READ MORE</a>
  </div>

  <aside class="blog abs">
    <h2>Blog Posts</h2>
    <div class="blog-thumb abs"></div>
    <div class="blog-post abs">
      <h3>Setrolis assa elit, auctor</h3>
      <p>Aliquam nibh ante, egestas id dictum a, commodo luctus libero.</p>
      <a class="more" href="#">READ MORE</a>
    </div>
  </aside>

  <footer class="site-footer abs">
    <div class="fcol abs" style="left:118px">
      <h4>Quick Links</h4>
      <ul><li>Home</li><li>Locations</li><li>Research</li><li>Sort me Out</li></ul>
    </div>
    <div class="fcol abs" style="left:228px;top:48px">
      <ul><li>Social</li><li>Blog</li><li>Bio</li></ul>
    </div>
    <div class="fcol abs" style="left:325px">
      <h4>Locations</h4>
      <ul><li>Setrolis assa elit</li><li>Master lam eget</li><li>Do nisi nibh ut semper</li><li>Sertloque</li></ul>
    </div>
    <div class="fcol abs" style="left:500px">
      <h4>Connect Us</h4>
      <ul>
        <li><span class="sicon"></span>Friendspace</li>
        <li><span class="sicon chirp"></span>Chirpline</li>
        <li><span class="sicon"></span>Linkwork</li>
        <li><span class="sicon rss"></span>Rss Feeds</li>
      </ul>
    </div>
    <div class="flogo abs">
      <span class="brand-mark"></span>
      <span class="brand-name">Brookfern<br>Clinical<br>Trials</span>
    </div>
    <div class="copyright abs">copyright 2015 Brookfern clinical, All right Reserved.</div>
  </footer>
</div>
</body>
</html>
```